Elm Ridge Baptist Church sign

We want a colourful, attractive sign that includes connection to being a Christian Church living in the foothills of the Canadian Rocky Mountains. As far as printed words, we need it to say “ Elm Ridge Baptist Church”. We are planning on a sign that is 6’ x 4’. Our church slogan is:
“ Live like Jesus, Love like Jesus”. This slogan could be included on the sign if space allows. To all designers; in talking with the communications team at our church, we want to eliminate the church’s slogan “ live like Jesus, live like Jesus “, from being on the sign.

```html
<!DOCTYPE html>
<html lang="en">
<head>
<meta charset="UTF-8">
<title>Elm Ridge Baptist Church Sign</title>
<link rel="stylesheet" href="https://fonts.googleapis.com/css2?family=Great+Vibes&display=swap">
<style>
  :root {
    --page: #ffffff;
    --ink: #ffffff;
    --sun: #f2f6fb;
    --sky-high: #2c9ad8;
    --sky-mid: #46abe4;
    --haze: #a7a9df;
    --ridge: #3d76c4;
    --valley: #2f8a9c;
    --field: #4f9c4a;
    --forest: #0f2c2b;
  }
  html, body {
    margin: 0;
    width: 1200px;
    height: 1200px;
    overflow: hidden;
    background: var(--page);
  }
  .canvas {
    position: relative;
    width: 1200px;
    height: 1200px;
  }
  .sign {
    position: absolute;
    left: 150px;
    top: 300px;
    width: 900px;
    height: 600px;
    overflow: hidden;
  }
  .sign-scene {
    position: absolute;
    inset: 0;
    background:
      radial-gradient(ellipse 340px 220px at 50% 0%, var(--sun) 0%, rgba(242,246,251,0.55) 35%, rgba(242,246,251,0) 100%),
      linear-gradient(to bottom,
        var(--sky-high) 0%,
        var(--sky-mid) 28%,
        var(--haze) 42%,
        #6f8fd6 52%,
        var(--ridge) 62%,
        #3472b4 72%,
        var(--valley) 78%,
        var(--field) 86%,
        #25553a 93%,
        var(--forest) 100%);
  }
  .sign-name {
    position: absolute;
    left: 0;
    right: 0;
    margin: 0;
    text-align: center;
    color: var(--ink);
    font-family: "Great Vibes", cursive;
    font-weight: 400;
    line-height: 1;
    white-space: nowrap;
  }
  .sign-name-top {
    top: 148px;
    font-size: 150px;
    letter-spacing: 4px;
  }
  .sign-name-bottom {
    top: 288px;
    font-size: 150px;
    letter-spacing: 2px;
  }
</style>
</head>
<body>
  <main class="canvas">
    <section class="sign">
      <div class="sign-scene" role="img" aria-label="Sun rays shining from a blue sky over snowy Rocky Mountain peaks, green foothills and a dark line of evergreen forest"></div>
      <h1 class="sign-name sign-name-top">Elm Ridge</h1>
      <p class="sign-name sign-name-bottom">Baptist Church</p>
    </section>
  </main>
</body>
</html>
```